Health Coaching Flyer for New Clients

I need a two-sided flyer (3.5" x 8.5" preferred or 5" x 7") to distribute to potential coaching clients. My business name is Talvery Health & Wellness Coaching. My business is focused on helping people with habit changes that contribute to their overall well-being. I would like the design colors to be gender neutral. I would like a small photo of myself near the "my name is Joan" statement. Please feel free to change the logo color to match the design.

Target Market(s)

Adults of all ages.

Font styles to use
Serif

Requirements
Must have
• Emphasize my opening question (found in health coaching brochure - attached).
• Small picture of myself near "my name is Joan" statement.
Should not have
• No light of pastel colors.

```html
<!DOCTYPE html>
<html lang="en">
<head>
<meta charset="utf-8">
<title>Talvery Health &amp; Wellness Coaching – Flyers</title>
<link rel="stylesheet" href="https://fonts.googleapis.com/css2?family=Bebas+Neue&family=Montserrat:wght@500;700;800&display=swap">
<style>
  :root {
    --stage: #2e2f33;
    --red: #d0313d;
    --red-deep: #c02a36;
    --red-light: #e0434f;
    --sky: #5bc8f0;
    --ribbon-blue: #1ea3dc;
    --navy: #1f3a6b;
    --ribbon-white: #f4f4f4;
    --brand-blue: #1a9bd7;
    --white: #ffffff;
    --mist-top: #c9c9cb;
    --mist-mid: #ededee;
    --shirt: #3b3c40;
    --slate: #6d6e70;
    --body-gray: #58595b;
    --logo-gray: #808285;
  }
  * { box-sizing: border-box; margin: 0; padding: 0; }
  html, body { width: 1200px; height: 849px; overflow: hidden; }
  body { background: var(--stage); position: relative; font-family: "Montserrat", sans-serif; }

  .flyer { position: absolute; top: 69px; width: 511px; height: 717px; background: var(--white); overflow: hidden; }
  .flyer--bold { left: 69px; }
  .flyer--soft { left: 609px; }

  .headline { position: absolute; font-family: "Bebas Neue", sans-serif; color: var(--white); line-height: 1; white-space: nowrap; }
  .headline small { font-family: "Montserrat", sans-serif; font-weight: 800; text-transform: none; }

  /* Bold red flyer */
  .flyer--bold .hero { position: absolute; inset: 0 0 270px 0; background: var(--red); }
  .flyer--bold .headline { top: 28px; left: 0; width: 100%; text-align: center; font-size: 94px; letter-spacing: -1px; }
  .flyer--bold .headline small { font-size: 22px; letter-spacing: 0; margin-left: 2px; }
  .flyer--bold .question { position: absolute; top: 108px; left: 0; width: 100%; text-align: center; font-weight: 800; font-size: 23.5px; line-height: 29px; color: var(--sky); }
  .flyer--bold .question .plain { color: var(--white); }
  .flyer--bold .illustration {
    position: absolute; left: 0; top: 177px; width: 100%; height: 270px;
    background:
      radial-gradient(ellipse 32% 45% at 12% 95%, var(--ribbon-white) 0%, rgba(244,244,244,0) 100%),
      radial-gradient(ellipse 26% 60% at 47% 60%, var(--ribbon-white) 0%, rgba(244,244,244,0) 100%),
      radial-gradient(ellipse 30% 45% at 42% 30%, var(--ribbon-blue) 0%, rgba(30,163,220,0) 100%),
      radial-gradient(ellipse 35% 35% at 55% 85%, var(--navy) 0%, rgba(31,58,107,0) 100%),
      radial-gradient(ellipse 20% 40% at 88% 25%, var(--ribbon-white) 0%, rgba(244,244,244,0) 100%),
      radial-gradient(ellipse 18% 45% at 30% 40%, var(--navy) 0%, rgba(31,58,107,0) 100%),
      linear-gradient(180deg, var(--red) 0%, var(--red-light) 60%, var(--red-deep) 100%);
  }
  .flyer--bold .portrait { position: absolute; left: 31px; top: 489px; width: 87px; height: 113px; background: linear-gradient(160deg, #7c6a5e, #b89a86 55%, #4a3a32); }
  .flyer--bold .intro { position: absolute; left: 132px; top: 487px; width: 362px; font-size: 12.6px; line-height: 17.2px; font-weight: 500; color: var(--navy); }
  .flyer--bold .brand { position: absolute; top: 638px; left: 0; width: 100%; text-align: center; color: var(--brand-blue); }
  .flyer--bold .base-band { position: absolute; left: 0; bottom: 0; width: 100%; height: 8px; background: var(--brand-blue); }

  /* Soft gray flyer */
  .flyer--soft .photo {
    position: absolute; inset: 0 0 198px 0;
    background:
      radial-gradient(ellipse 45% 40% at 72% 100%, var(--shirt) 0%, rgba(59,60,64,0.6) 55%, rgba(59,60,64,0) 100%),
      radial-gradient(ellipse 28% 26% at 70% 46%, var(--white) 0%, rgba(255,255,255,0) 100%),
      linear-gradient(180deg, var(--mist-top) 0%, var(--mist-mid) 55%, #e4e4e5 100%);
  }
  .flyer--soft .headline { top: 42px; left: 26px; font-size: 104px; letter-spacing: -1.5px; }
  .flyer--soft .headline small { font-size: 22px; letter-spacing: 0; color: var(--slate); margin-left: 2px; }
  .flyer--soft .question { position: absolute; top: 137px; left: 27px; font-weight: 800; font-size: 23.5px; line-height: 29px; color: var(--slate); }
  .flyer--soft .color-rule { position: absolute; left: 29px; top: 285px; }
  .flyer--soft .photo-frame { position: absolute; left: 18px; top: 501px; width: 101px; height: 129px; background: var(--white); }
  .flyer--soft .portrait { position: absolute; left: 25px; top: 509px; width: 87px; height: 113px; background: linear-gradient(160deg, #7c6a5e, #b89a86 55%, #4a3a32); }
  .flyer--soft .intro { position: absolute; left: 132px; top: 531px; width: 366px; font-size: 11.2px; line-height: 15.7px; font-weight: 500; color: var(--body-gray); }
  .flyer--soft .brand { position: absolute; top: 648px; right: 28px; text-align: right; color: var(--logo-gray); }

  .brand { font-family: "Montserrat", sans-serif; font-weight: 800; font-size: 15px; letter-spacing: 0.3px; line-height: 1.2; }
  .brand span { display: block; font-size: 30px; letter-spacing: 2px; }
</style>
</head>
<body>

  <section class="flyer flyer--bold">
    <div class="hero"></div>
    <h1 class="headline">NEED SUPPORT<small>in</small></h1>
    <p class="question">MAKING REAL, LASTING LIFESTYLE<br><span class="plain">and</span> BEHAVIOR CHANGES?</p>
    <div class="illustration" role="img" aria-label="Illustration of a businessman on a hill pointing toward twisting blue and white ribbons that rise into upward arrows"></div>
    <div class="portrait" role="img" aria-label="Portrait photo of Joan, the health coach"></div>
    <p class="intro">My name is Joan.&nbsp; I am studying to become an THRIVE-Certified Functional Health Coach.&nbsp; My training involves many science-based practices that improve both our health and how we grow and change as humans.&nbsp; I now have the opportunity to turn that knowledge into practice by coaching actual clients interested in improving their own health and well-being.</p>
    <div class="brand"><span>TALVERY</span>HEALTH &amp; WELLNESS COACHING</div>
    <div class="base-band"></div>
  </section>

  <section class="flyer flyer--soft">
    <div class="photo" role="img" aria-label="Photo of a woman in a dark top holding a hand-drawn smiley face sign in front of her face"></div>
    <h1 class="headline">NEED SUPPORT<small>in</small></h1>
    <p class="question">MAKING REAL,<br>LASTING<br>LIFESTYLE and<br>BEHAVIOR<br>CHANGES?</p>
    <svg class="color-rule" width="131" height="3" viewBox="0 0 131 3" aria-hidden="true">
      <rect x="0" width="10" height="3" fill="#6a4c9c"/>
      <rect x="15" width="10" height="3" fill="#e0348a"/>
      <rect x="30" width="10" height="3" fill="#ee4236"/>
      <rect x="45" width="10" height="3" fill="#1ba5dd"/>
      <rect x="60" width="10" height="3" fill="#17b8a6"/>
      <rect x="75" width="10" height="3" fill="#5bb947"/>
      <rect x="90" width="10" height="3" fill="#a6ce39"/>
      <rect x="105" width="10" height="3" fill="#f7941d"/>
      <rect x="120" width="10" height="3" fill="#f2d600"/>
    </svg>
    <div class="photo-frame"></div>
    <div class="portrait" role="img" aria-label="Portrait photo of Joan, the health coach"></div>
    <p class="intro">My name is Joan.&nbsp; I am studying to become an THRIVE-Certified Functional Health Coach.&nbsp; My training involves many science-based practices that improve both our health and how we grow and change as humans.&nbsp; I now have the opportunity to turn that knowledge into practice by coaching actual clients interested in improving their own health and well-being.</p>
    <div class="brand"><span>TALVERY</span>HEALTH &amp; WELLNESS COACHING</div>
  </section>

</body>
</html>
```